Tarvo Computer Repairs Web Banner

We're after a catchy web banner to advertise the computer repairs business on other web sites and affiliate sites. We manage software, hardware repairs, component upgrades, virus and malware removal and provide online backup solutions.
Please incorporate the logo designed by Ravex, and add our phone number, 1300 482 956 to the banner. The banner will link to the website homepage.

```html
<!DOCTYPE html>
<html lang="en">
<head>
<meta charset="utf-8">
<title>Tarvo Computer Repairs – Web Banner</title>
<link rel="stylesheet" href="https://fonts.googleapis.com/css2?family=Anton&display=swap">
<style>
  :root {
    --ink: #0d0d0d;
    --band: #1b1b1b;
    --maroon: #8c2b2b;
    --dusk: #141212;
    --glow: #ffffff;
    --gold-top: #fff46a;
    --gold-bottom: #f7c400;
    --brand-blue: #2a57a8;
    --white: #ffffff;
  }
  html, body {
    margin: 0;
    padding: 0;
    width: 1200px;
    height: 1000px;
    overflow: hidden;
    background: var(--ink);
  }
  .banner {
    display: block;
    width: 1200px;
    height: 1000px;
    text-decoration: none;
  }
  .banner svg {
    display: block;
    width: 1200px;
    height: 1000px;
  }
  .headline,
  .service,
  .phone-number {
    font-family: "Anton", "Oswald", Impact, sans-serif;
    paint-order: stroke fill;
    stroke-linejoin: round;
  }
  .headline,
  .service {
    fill: url(#goldFill);
    stroke: var(--ink);
  }
  .headline { stroke-width: 16px; font-size: 150px; }
  .service { stroke-width: 12px; font-size: 80px; }
  .phone-number {
    fill: var(--brand-blue);
    stroke: var(--white);
    stroke-width: 14px;
    font-size: 178px;
  }
  .brand-name {
    font-family: "Anton", "Oswald", Impact, sans-serif;
    font-size: 54px;
    fill: var(--brand-blue);
  }
  .brand-mark { fill: var(--brand-blue); }
  .phone-icon {
    fill: var(--brand-blue);
    stroke: var(--white);
    stroke-width: 1.3px;
    paint-order: stroke fill;
    stroke-linejoin: round;
  }
</style>
</head>
<body>
<a class="banner" href="/" aria-label="Tarvo Computer Repairs – call 1300 482 956">
  <svg viewBox="0 0 1200 1000" xmlns="http://www.w3.org/2000/svg">
    <defs>
      <linearGradient id="backdrop" x1="0" y1="0" x2="0" y2="1">
        <stop offset="0" stop-color="var(--dusk)"/>
        <stop offset="0.35" stop-color="#2a1a1a"/>
        <stop offset="1" stop-color="var(--maroon)"/>
      </linearGradient>
      <radialGradient id="spotlight" cx="270" cy="290" r="300" gradientUnits="userSpaceOnUse">
        <stop offset="0" stop-color="var(--glow)"/>
        <stop offset="0.45" stop-color="var(--glow)" stop-opacity="0.85"/>
        <stop offset="1" stop-color="var(--glow)" stop-opacity="0"/>
      </radialGradient>
      <linearGradient id="goldFill" x1="0" y1="0" x2="0" y2="1">
        <stop offset="0" stop-color="var(--gold-top)"/>
        <stop offset="1" stop-color="var(--gold-bottom)"/>
      </linearGradient>
    </defs>

    <!-- backdrop -->
    <rect class="backdrop" x="0" y="0" width="1200" height="785" fill="url(#backdrop)"/>
    <rect class="spotlight" x="0" y="0" width="600" height="620" fill="url(#spotlight)"/>
    <rect class="contact-band" x="0" y="785" width="1200" height="215" fill="var(--band)"/>

    <!-- brand -->
    <g class="brand">
      <circle class="brand-mark" cx="270" cy="200" r="80"/>
      <text class="brand-name" x="270" y="370" text-anchor="middle">Tarvo</text>
      <text class="brand-name" x="270" y="435" text-anchor="middle">Computer</text>
      <text class="brand-name" x="270" y="500" text-anchor="middle">Repairs</text>
    </g>

    <!-- headline services -->
    <g class="headlines">
      <text class="headline" x="512" y="168" textLength="638" lengthAdjust="spacingAndGlyphs">SOFTWARES</text>
      <text class="headline" x="520" y="368" textLength="625" lengthAdjust="spacingAndGlyphs">REPAIRS</text>
      <text class="headline" x="512" y="540" textLength="638" lengthAdjust="spacingAndGlyphs">UPGRADES</text>
    </g>

    <g class="services">
      <text class="service" x="28" y="648" textLength="1137" lengthAdjust="spacingAndGlyphs">VIRUS AND MALWARE REMOVAL</text>
      <text class="service" x="28" y="754" textLength="1137" lengthAdjust="spacingAndGlyphs">ONLINE BACKUP SOLUTIONS</text>
    </g>

    <!-- contact -->
    <g class="contact">
      <path class="phone-icon" transform="translate(22 808) scale(7.2)"
        d="M6.62 10.79c1.44 2.83 3.76 5.14 6.59 6.59l2.2-2.2c.27-.27.67-.36 1.02-.24 1.12.37 2.33.57 3.57.57.55 0 1 .45 1 1V20c0 .55-.45 1-1 1-9.39 0-17-7.61-17-17 0-.55.45-1 1-1h3.5c.55 0 1 .45 1 1 0 1.25.2 2.45.57 3.57.11.35.03.74-.25 1.02l-2.2 2.2z"/>
      <text class="phone-number" x="182" y="980" textLength="985" lengthAdjust="spacingAndGlyphs">1300 482 956</text>
    </g>
  </svg>
</a>
</body>
</html>
```